business stationery

have a gorgeous logo that needs to be incorporated on stationery. Was hoping to do something on letterhead that was a paper that looked like "bark" from a tree or something that resembled the "woods." Soft paper with some very basic natural elements. Same thing for business cards. Think American lakeside cabin. Organic. Natural. Calm and welcoming but clear to read and understand. Wanted to use alot of black.

Target Market(s)

buyers of Tobias Wrenfield home. Client that would have more than one home and in need of rare pieces and items to furnish an upmarket lakeside holiday cabin in the woods. Someone who treasures beautiful hand made items, organic foods and a real crackling fire but with money to burn in it!

Industry/Entity Type

Business

Requirements
Must have
• My logo
My business name
www.fernandcopper.example
Natural almost raw effect paper
My ABN: 62 307 514 928 (to be placed in small writing at the bottom of card/letterhead)
Nice to have
• The website will consist of a cabin door that you "open" with a creak sound effect and then you go "inside" to look at the various rooms to start shopping. Want to bring that element of texture and warmth into the stationary also.
Should not have
• Anything modern or hard to read items

```html
<!DOCTYPE html>
<html lang="en">
<head>
<meta charset="utf-8">
<title>Fern &amp; Copper – Business Card</title>
<link rel="stylesheet" href="https://fonts.googleapis.com/css2?family=Arimo:wght@400;700&display=swap">
<style>
  :root {
    --page: #ffffff;
    --paper-light: #d3c29f;
    --paper-mid: #c6b38d;
    --paper-dark: #b5a07a;
    --fibre-light: #e6dac0;
    --fibre-dark: #9c8762;
    --ink: #1b1714;
    --ink-soft: #2a241f;
    --maple: #7a1f1c;
  }
  * { box-sizing: border-box; margin: 0; padding: 0; }
  html, body {
    width: 1200px;
    height: 405px;
    overflow: hidden;
    background: var(--page);
    font-family: "Arimo", Arial, sans-serif;
    color: var(--ink);
  }
  .defs { position: absolute; width: 0; height: 0; }
  .stage { position: relative; width: 1200px; height: 405px; }

  .card {
    position: absolute;
    width: 514px;
    height: 228px;
    border-radius: 14px;
    background:
      radial-gradient(ellipse at 25% 30%, var(--paper-light) 0%, transparent 60%),
      radial-gradient(ellipse at 80% 75%, var(--paper-dark) 0%, transparent 65%),
      var(--paper-mid);
    overflow: hidden;
    box-shadow: 0 8px 18px rgba(0,0,0,0.12);
  }
  .card--front { left: 48px; top: 60px; }
  .card--back  { left: 614px; top: 52px; }

  .paper-fibres {
    position: absolute;
    inset: 0;
    width: 514px;
    height: 228px;
  }
  .paper-fibres .light { stroke: var(--fibre-light); stroke-width: 1; opacity: 0.75; fill: none; }
  .paper-fibres .dark  { stroke: var(--fibre-dark);  stroke-width: 0.8; opacity: 0.55; fill: none; }

  .brand { position: absolute; display: flex; flex-direction: column; align-items: flex-start; }
  .brand__row { display: flex; align-items: center; gap: 4px; }
  .brand__dot { width: 9px; height: 9px; border-radius: 50%; background: var(--maple); }
  .brand__name {
    font-weight: 700;
    font-size: 16px;
    letter-spacing: -0.4px;
    line-height: 1;
    color: var(--ink);
  }
  .brand__tagline {
    margin-left: 13px;
    margin-top: 2px;
    font-size: 5px;
    letter-spacing: 0.5px;
    text-transform: uppercase;
    color: var(--maple);
  }
  .card--front .brand { left: 34px; top: 138px; }
  .card--back .brand  { left: 26px; top: 52px; }

  .branch-art {
    position: absolute;
    left: 205px;
    top: 30px;
    width: 309px;
    height: 165px;
    border-radius: 82px 0 0 82px;
    background: linear-gradient(90deg, rgba(27,23,20,0.18) 0%, rgba(27,23,20,0.55) 55%, rgba(27,23,20,0.85) 100%);
  }

  .contact { position: absolute; left: 172px; top: 80px; line-height: 1.12; }
  .contact__name { font-weight: 700; font-size: 15px; margin-bottom: 2px; }
  .contact__line { font-size: 12.5px; color: var(--ink-soft); }
  .abn { position: absolute; right: 30px; top: 186px; font-size: 12px; color: var(--ink-soft); }
</style>
</head>
<body>
  <svg class="defs" aria-hidden="true">
    <symbol id="fibres" viewBox="0 0 514 228">
      <path class="light" d="M20 30 l38 6 M70 12 l22 18 M120 60 l48 -4 M200 20 l30 12 M260 70 l44 8 M330 18 l26 20 M400 50 l52 -6 M470 24 l24 14"/>
      <path class="light" d="M30 110 l40 10 M96 150 l30 -14 M150 200 l46 4 M240 130 l20 22 M300 190 l50 -8 M380 120 l34 16 M440 180 l40 6 M60 190 l26 18"/>
      <path class="dark" d="M48 70 l24 -10 M110 100 l36 14 M180 160 l18 20 M230 96 l40 -6 M290 40 l18 16 M350 150 l42 10 M420 90 l30 -12 M480 140 l20 22"/>
      <path class="dark" d="M12 170 l34 -6 M130 30 l20 8 M210 210 l30 -10 M320 100 l28 4 M390 200 l24 -14 M460 60 l30 10"/>
    </symbol>
  </svg>

  <main class="stage">
    <section class="card card--front" aria-label="Business card front">
      <svg class="paper-fibres" aria-hidden="true"><use href="#fibres"/></svg>
      <div class="brand">
        <div class="brand__row">
          <span class="brand__dot"></span>
          <span class="brand__name">FERN &amp; COPPER</span>
        </div>
        <span class="brand__tagline">Lakeside home</span>
      </div>
      <div class="branch-art" role="img" aria-label="Black swirling tree branch illustration with scattered red maple leaves"></div>
    </section>

    <section class="card card--back" aria-label="Business card back">
      <svg class="paper-fibres" aria-hidden="true"><use href="#fibres"/></svg>
      <div class="brand">
        <div class="brand__row">
          <span class="brand__dot"></span>
          <span class="brand__name">FERN &amp; COPPER</span>
        </div>
        <span class="brand__tagline">Lakeside home</span>
      </div>
      <div class="contact">
        <p class="contact__name">Callum Ashby</p>
        <p class="contact__line">cashby@fernandcopper.example</p>
        <p class="contact__line">www.fernandcopper.example</p>
      </div>
      <p class="abn">ABN: 62 307 514 928</p>
    </section>
  </main>
</body>
</html>
```